International Company needs a Letterhead & Envelope Design

Our Company name is Corvale Brightwick Limited.
We'd like to ask the Designers for the luxurious and sophisticated design. Our logo is very simple and neat with letter logos, so we look forward to more professional and refined designs from Designers.
We look forward to providing you with a great design.
Thanks very much in advance.

```html
<!DOCTYPE html>
<html lang="en">
<head>
<meta charset="utf-8">
<title>Corvale Brightwick Limited — Stationery</title>
<link rel="stylesheet" href="https://fonts.googleapis.com/css2?family=Roboto:wght@400;500;700&display=swap">
<style>
  :root {
    --ink: #0b0b0b;
    --paper: #ffffff;
    --stage: #ececec;
    --mark-grey: #5d5d5d;
    --rule: #9a9a9a;
    --text: #222222;
  }
  * { box-sizing: border-box; margin: 0; padding: 0; }
  html, body { width: 1200px; height: 858px; overflow: hidden; }
  body {
    background: var(--stage);
    font-family: "Roboto", Arial, sans-serif;
    color: var(--text);
    position: relative;
  }
  .sheet { position: absolute; overflow: hidden; box-shadow: 0 2px 6px rgba(0,0,0,.18); }
  .sheet svg.swoosh { position: absolute; inset: 0; width: 100%; height: 100%; }
  .brand {
    font-family: "Roboto", Arial, sans-serif;
    font-weight: 700;
    text-transform: uppercase;
    letter-spacing: .04em;
    line-height: 1;
    white-space: nowrap;
    color: var(--ink);
  }
  .brand.on-dark { color: var(--mark-grey); }

  /* Letterhead */
  .letterhead { left: 40px; top: 36px; width: 330px; height: 467px; background: var(--paper); }
  .letterhead .brand { position: absolute; left: 24px; top: 58px; font-size: 15px; }
  .recipient { position: absolute; left: 24px; top: 92px; font-size: 5.5px; line-height: 1.4; }
  .recipient strong { font-weight: 700; font-size: 6px; }
  .letter-body { position: absolute; left: 24px; top: 124px; width: 232px; font-size: 6px; line-height: 1.55; }
  .letter-body p { margin-bottom: 7px; }
  .signature { position: absolute; left: 24px; top: 278px; width: 70px; height: 18px; background: linear-gradient(90deg, #d8d8d8, #ececec); border-radius: 2px; }
  .signer { position: absolute; left: 24px; top: 302px; font-size: 6px; line-height: 1.4; }
  .signer strong { font-weight: 700; }
  .letter-footer { position: absolute; left: 24px; top: 352px; display: flex; gap: 8px; font-size: 5.5px; line-height: 1.7; }
  .letter-footer .divider { width: 1px; background: var(--ink); }
  .contact-row { display: flex; align-items: center; gap: 3px; }
  .contact-row svg { width: 6px; height: 6px; fill: var(--ink); }

  /* Letterhead reverse */
  .letter-reverse { left: 400px; top: 36px; width: 330px; height: 467px; background: var(--ink); }
  .letter-reverse .brand { position: absolute; left: 0; right: 0; top: 70px; text-align: center; font-size: 18px; }

  /* Envelopes */
  .envelope-front { left: 760px; top: 36px; width: 400px; height: 200px; background: var(--paper); }
  .envelope-front .brand { position: absolute; left: 34px; top: 72px; font-size: 19px; }
  .envelope-address { position: absolute; left: 34px; top: 138px; padding-left: 6px; border-left: 1px solid var(--ink); font-size: 6px; line-height: 1.5; }
  .envelope-back { left: 760px; top: 256px; width: 400px; height: 200px; background: var(--paper); }
  .envelope-flap { position: absolute; left: 0; top: 0; width: 100%; height: 62px; background: var(--ink); border-bottom-right-radius: 26px; }
  .envelope-back .brand { position: absolute; left: 0; right: 0; top: 24px; text-align: center; font-size: 13px; }

  /* Business cards */
  .card-front { left: 760px; top: 476px; width: 190px; height: 108px; background: var(--paper); }
  .card-front .brand { position: absolute; right: 12px; top: 14px; font-size: 9px; }
  .card-details { position: absolute; left: 62px; top: 40px; font-size: 5px; line-height: 1.5; }
  .card-details strong { font-size: 6px; font-weight: 700; }
  .card-back { left: 970px; top: 476px; width: 190px; height: 108px; background: var(--ink); }
  .card-back .brand { position: absolute; left: 0; right: 0; top: 48px; text-align: center; font-size: 11px; }

  /* Notebook */
  .notebook { left: 40px; top: 530px; width: 230px; height: 300px; background: var(--ink); }
  .notebook .spiral { position: absolute; left: 6px; top: 10px; bottom: 10px; width: 8px;
    background: radial-gradient(circle, #bdbdbd 2px, transparent 2.5px) 0 0 / 8px 10px repeat-y; }
  .notebook .brand { position: absolute; left: 0; right: 0; top: 70px; text-align: center; font-size: 13px; }

  /* Key tag and eraser */
  .keytag { left: 320px; top: 580px; width: 130px; height: 72px; background: var(--ink); border: 4px solid #d6d6d6; border-radius: 8px; }
  .keytag .brand { position: absolute; left: 0; right: 0; top: 26px; text-align: center; font-size: 8px; }
  .key-ring { position: absolute; left: 366px; top: 540px; width: 38px; height: 38px; border: 3px solid #b8b8b8; border-radius: 50%; }
  .eraser { left: 320px; top: 690px; width: 130px; height: 44px; background: var(--ink); border-left: 26px solid #f4f4f4; }
  .eraser .brand { position: absolute; left: 0; right: 0; top: 18px; text-align: center; font-size: 7px; }
</style>
</head>
<body>

  <!-- Letterhead -->
  <section class="sheet letterhead">
    <svg class="swoosh" viewBox="0 0 330 467" preserveAspectRatio="none" aria-hidden="true">
      <path d="M330 172 C310 252 280 322 230 372 C170 422 90 440 0 444" fill="none" stroke="var(--rule)" stroke-width="1"/>
      <path d="M330 180 C310 260 280 330 230 380 C170 430 90 448 0 452 L0 467 L330 467 Z" fill="var(--ink)"/>
    </svg>
    <div class="brand">Corvale Brightwick</div>
    <div class="recipient">
      <strong>ALDEN MARSH</strong><br>Street Name City Name<br>Zip Code 0000
    </div>
    <div class="letter-body">
      <p>We are pleased to confirm our partnership for the coming year and look forward to working closely with your team. Our offices will share a full schedule of meetings, deliverables and review dates shortly, so that every stage is planned with care.</p>
      <p>Please contact us at any time should you need further details. We value your trust and remain committed to quality, clarity and prompt service across all of our regions.</p>
      <p>Regards,</p>
    </div>
    <div class="signature" role="img" aria-label="Handwritten signature"></div>
    <div class="signer"><strong>Priya Okafor</strong><br><strong>General Manager</strong></div>
    <div class="letter-footer">
      <div>
        <div class="contact-row"><svg viewBox="0 0 10 10"><path d="M2 1h2l1 2-1 1c.5 1 1.5 2 2.5 2.5l1-1 2 1v2c-4 0-7.5-3.5-7.5-7.5z"/></svg>1 (555) 014-2290</div>
        <div class="contact-row"><svg viewBox="0 0 10 10"><rect x="2.5" y="0.5" width="5" height="9" rx="1"/></svg>1 (555) 014-7731</div>
        <div class="contact-row"><svg viewBox="0 0 10 10"><path d="M0 2h10v6H0z"/></svg>hello@corvalebrightwick.com</div>
      </div>
      <div class="divider"></div>
      <div>Unit 4 Harlow Business Park<br>18 Fenwick Road<br>Easton 12</div>
    </div>
  </section>

  <!-- Letterhead reverse -->
  <section class="sheet letter-reverse">
    <div class="brand on-dark">Corvale Brightwick</div>
  </section>

  <!-- Envelope front -->
  <section class="sheet envelope-front">
    <svg class="swoosh" viewBox="0 0 400 200" preserveAspectRatio="none" aria-hidden="true">
      <path d="M400 0 L372 0 C360 70 330 150 240 178 C170 192 80 192 0 192 L0 200 L400 200 Z" fill="var(--ink)"/>
    </svg>
    <div class="brand">Corvale Brightwick</div>
    <div class="envelope-address">Unit 4 Harlow Business Park<br>18 Fenwick Road<br>Easton 12</div>
  </section>

  <!-- Envelope back -->
  <section class="sheet envelope-back">
    <div class="envelope-flap"></div>
    <div class="brand on-dark">Corvale Brightwick</div>
  </section>

  <!-- Business card front -->
  <section class="sheet card-front">
    <svg class="swoosh" viewBox="0 0 190 108" preserveAspectRatio="none" aria-hidden="true">
      <path d="M0 0 L0 108 L70 108 C50 90 44 40 72 0 Z" fill="var(--ink)"/>
    </svg>
    <div class="brand">Corvale Brightwick</div>
    <div class="card-details">
      <strong>Tomas Reyes</strong> · Director<br>
      Unit 4 Harlow Business Park<br>
      18 Fenwick Road, Easton 12<br>
      1 (555) 014-2290<br>
      hello@corvalebrightwick.com
    </div>
  </section>

  <!-- Business card back -->
  <section class="sheet card-back">
    <div class="brand on-dark">Corvale Brightwick</div>
  </section>

  <!-- Notebook -->
  <section class="sheet notebook">
    <div class="spiral"></div>
    <div class="brand on-dark">Corvale Brightwick</div>
  </section>

  <!-- Key tag -->
  <div class="key-ring"></div>
  <section class="sheet keytag">
    <div class="brand on-dark">Corvale Brightwick</div>
  </section>

  <!-- Eraser -->
  <section class="sheet eraser">
    <div class="brand on-dark">Corvale Brightwick</div>
  </section>

</body>
</html>
```